3 x 3 metre trade booth design

We need a design for a 3 x 3 metre corner booth for a conference we are attending. There will therefore be 2 x backdrops that we need to have designed. For one of them we want to have our services displayed as an engaging, modern infographic. For the other, we would like to have our brand tagline and our logo, with a cool background which aligns with what we do.
I have attached a picture of what our booth looked like last year- we designed this ourself and we need it to look much more professional, with a different type of infographic for the
Please see attachment with full design brief attached

```html
<!DOCTYPE html>
<html lang="en">
<head>
<meta charset="utf-8">
<title>Vantora corner booth backdrops</title>
<link rel="stylesheet" href="https://fonts.googleapis.com/css2?family=Roboto+Condensed:wght@700&family=Roboto:wght@400;700&display=swap">
<style>
  :root {
    --stage: #6b6b6b;
    --ink: #2b2a2f;
    --purple: #8e55a8;
    --gold: #e8bd3a;
    --shade: #dcdcdc;
    --paper: #ffffff;
    --body: #333333;
  }
  html, body { margin: 0; padding: 0; overflow: hidden; }
  body { width: 967px; height: 1200px; background: var(--stage); position: relative; }
  .backdrop { position: absolute; left: 203px; width: 560px; height: 560px; display: block; }
  .backdrop--services { top: 30px; }
  .backdrop--tagline { top: 610px; }
  .display { font-family: "Roboto Condensed", "Arial Narrow", sans-serif; font-weight: 700; }
  .service-title { font-family: "Roboto", Arial, sans-serif; font-weight: 700; font-size: 13px; fill: var(--purple); }
  .service-item { font-family: "Roboto", Arial, sans-serif; font-size: 8.6px; fill: var(--body); }
  .web-address { font-family: "Roboto", Arial, sans-serif; font-weight: 700; font-size: 16px; fill: var(--paper); }
  .brand-name { font-family: "Roboto Condensed", "Arial Narrow", sans-serif; font-weight: 700; font-size: 15px; fill: var(--paper); letter-spacing: 4px; }
</style>
</head>
<body>

<svg class="backdrop backdrop--services" viewBox="0 0 528 528" aria-label="Full service management backdrop">
  <rect width="528" height="528" fill="var(--paper)"/>
  <path class="wave-purple" d="M0,256 C8,372 120,424 300,452 C430,472 500,490 528,528 L0,528 Z" fill="var(--purple)"/>
  <path class="wave-gold" d="M0,264 C8,380 120,432 300,460 C425,480 492,498 514,528 L0,528 Z" fill="var(--gold)"/>
  <path class="wave-ink" d="M0,270 C10,388 130,440 300,468 C420,488 478,505 498,528 L0,528 Z" fill="var(--ink)"/>

  <text class="display" x="264" y="74" text-anchor="middle" font-size="30" fill="var(--ink)">FULL SERVICE MANAGEMENT</text>
  <line x1="116" y1="82" x2="412" y2="82" stroke="var(--ink)" stroke-width="2"/>

  <line x1="264" y1="104" x2="264" y2="194" stroke="var(--ink)" stroke-width="2.5"/>
  <line x1="264" y1="272" x2="264" y2="420" stroke="var(--ink)" stroke-width="2.5"/>

  <g text-anchor="end">
    <text class="service-title" x="220" y="124">Nimbuy Account Setup</text>
    <text class="service-item" x="220" y="144">
      <tspan x="220">Cost analysis to scale profitably</tspan>
      <tspan x="220" dy="10.7">Nimbuy account setup</tspan>
      <tspan x="220" dy="10.7">Account audit</tspan>
      <tspan x="220" dy="10.7">Nimbuy Brand Registry</tspan>
    </text>
    <text class="service-title" x="220" y="297">Account Management</text>
    <text class="service-item" x="220" y="317">
      <tspan x="220">Catalogue management</tspan>
      <tspan x="220" dy="10.7">Account health monitoring</tspan>
      <tspan x="220" dy="10.7">Case log &amp; issue resolution</tspan>
      <tspan x="220" dy="10.7">Warehouse Inventory Management</tspan>
      <tspan x="220" dy="10.7">Customised Reporting</tspan>
    </text>
  </g>

  <g text-anchor="start">
    <text class="service-title" x="306" y="124">International Expansion</text>
    <text class="service-item" x="306" y="144">
      <tspan x="306">Market opportunity analysis</tspan>
      <tspan x="306" dy="10.7">Launch in new marketplaces</tspan>
      <tspan x="306" dy="10.7">Listing localisation</tspan>
      <tspan x="306" dy="10.7">Logistics &amp; Fulfilment strategy</tspan>
    </text>
    <text class="service-title" x="306" y="297">Brand Content &amp; Optimisation</text>
    <text class="service-item" x="306" y="317">
      <tspan x="306">Rich Content / Enhanced Brand Content</tspan>
      <tspan x="306" dy="10.7">Brand store</tspan>
      <tspan x="306" dy="10.7">Product listing optimisation</tspan>
      <tspan x="306" dy="10.7">Search Engine Optimisation (SEO)</tspan>
    </text>
  </g>

  <g text-anchor="middle">
    <text class="service-title" x="264" y="216">Nimbuy Advertising</text>
    <text class="service-item" x="264" y="236">
      <tspan x="264">Sponsored Ads (PPC)</tspan>
      <tspan x="264" dy="10.7">Bid automation</tspan>
      <tspan x="264" dy="10.7">Demand-Side Platform (DSP)</tspan>
    </text>
  </g>

  <circle class="brand-dot" cx="48" cy="483" r="18" fill="var(--gold)"/>
  <text class="web-address" x="80" y="490">www.vantora.com</text>
</svg>

<svg class="backdrop backdrop--tagline" viewBox="0 0 528 528" aria-label="Tagline backdrop">
  <defs>
    <linearGradient id="featureTone" x1="0" y1="0" x2="0.6" y2="1">
      <stop offset="0" stop-color="var(--purple)" stop-opacity="0.35"/>
      <stop offset="1" stop-color="var(--gold)" stop-opacity="0.45"/>
    </linearGradient>
  </defs>
  <rect width="528" height="528" fill="var(--paper)"/>
  <rect class="feature-art" x="33" y="192" width="290" height="336" fill="url(#featureTone)" role="img" aria-label="Large brand feature artwork in purple to gold tones"/>
  <polygon class="stripe-shade" points="238,18 258,18 472,528 452,528" fill="var(--shade)"/>
  <polygon class="stripe-shade" points="262,150 282,150 476,528 456,528" fill="var(--shade)"/>
  <polygon class="panel-ink" points="250,0 528,0 528,528 500,528" fill="var(--ink)"/>
  <polygon class="stripe-gold" points="255,48 275,48 440,352 420,352" fill="var(--gold)"/>
  <polygon class="stripe-purple" points="278,152 306,152 528,500 528,528 498,528" fill="var(--purple)"/>

  <text class="display" x="30" y="88" font-size="30" fill="var(--purple)">TRANSFORMING</text>
  <text class="display" x="30" y="122" font-size="30" fill="var(--gold)">BRANDS</text>
  <text class="display" x="31" y="146" font-size="17" fill="var(--ink)">INTO NIMBUY SUCCESS STORIES</text>

  <rect class="brand-square" x="318" y="48" width="16" height="16" fill="var(--gold)"/>
  <text class="brand-name" x="344" y="63">VANTORA</text>
</svg>

</body>
</html>
```